Varimel Sciences needs high end Label Design for a revolutionary new supplement

We at Varimel Sciences are looking for a brand new Label Design for a first of its kind product called Morivane. It is the first supplement on the market that treats grief and heartbreak. This product is unisex for both men and woman. We want the New Label to look high end and luxurious using the brand colors which are gold and burgundy. Please feel free to use other colors such as black, white, or gray to go along with it or any other colors if you feel would be a great fit! Varimel Sciences is like the Zephlon of the supplement world, coming out with new products that will challenge the way people treat different symptoms. To Recap:

1. Product Name: MORIVANE - the font will play a big roll
2. The Label will be placed on an all white bottle
3. Some parts of the label will be printed with foil to make parts of the label shiny and more attractive. Please keep this in mind when designing.
4. Must use our Logo. I will attach a file of our logo and of the emblem as well. Feel free to use the emblem separately if you have a great idea for it. Please let us know if you need the Logo in a different file type.
5. This all natural herbal supplement in pill form is the first to treat grief and support someone with a broken heart. The consumers purchasing this product will be going through a hard and emotional time. This is a serious product.
6. The manufacturer has included some basic instructions regarding the dye line and file types. Please do your best to meet these. If you cannot meet the guidelines please submit art work anyways. If your design is chosen we will just have the manufacturer replicate the design.

The final label should portray Morivane and Varimel Sciences as a luxurious brand and product which was made with cutting edge science leading the way with revolutionary ideas. We want customers to feel that the product is worth every penny, because it is. As soon as they receive the product and take one look at the label, I want them to think WOW I made the right choice buying this. I have attached some Label designs that we really liked for your review.

Please feel free to message me with any questions or if you need the Logo in a different file type. Thank you all.
Updates

Please send in more entries while we take a couple days to review, we are still looking for that one design we can work with. We are getting close, thank you all!

Target Market(s)

People going through grief and heartbreak.

Font styles to use
Sans Serif
Script
Other font styles liked:
• Any font that looks good, The font for the name MORIVANE is very important and will brand it. We hated the font used in the label we received in our first label draft (attached so you can see)

Requirements
Must have
• Must have the company Logo that says the company name
• Must have the colors Gold and Burgundy
• Must have some areas that will be the shiny foil when label is printed.
• Must say "Dietary Supplement" somewhere near the bottom along with "90 Capsules"
• I have attached a Label someone designed for us but were not really happy with. I did like the font the "Dietary supplement" and "90 Capsules" had and also where it was placed. We absolutely HATED the font used for Morivane.
• Must look at the label design we received from the manufacturer and take into consideration the room needed to write in the directions and all the symbols such as "made in america" and "QPA Facility" Don't worry about adding these in as they will put those in before printing but keep in mind they will be added to the Final Label along with the Supplement Facts.
Nice to have
• Would like to see other colors to go with gold and burgundy suck as black, white, or gray. I have attached some Label designs that I really liked for your reference.
Should not have
• Does not need to have any other legal language, that will be applied by the the manufacturer's graphics team.

```html
<!DOCTYPE html>
<html lang="en">
<head>
<meta charset="utf-8">
<title>Morivane – Dietary Supplement Label</title>
<link href="https://fonts.googleapis.com/css2?family=Josefin+Sans:wght@300&family=Montserrat:wght@500;700&display=swap" rel="stylesheet">
<style>
  :root {
    --backdrop: #f4f3f1;
    --label-black: #141112;
    --burgundy: #5e1424;
    --burgundy-deep: #2a0a11;
    --foil-gold: #c9a44c;
    --foil-gold-light: #e8c877;
    --foil-gold-deep: #9c7a2e;
    --ink-white: #f4f4f2;
  }
  html, body {
    margin: 0;
    padding: 0;
    width: 1200px;
    height: 1200px;
    overflow: hidden;
    background: var(--backdrop);
  }
  .label {
    position: absolute;
    left: 100px;
    top: 80px;
    width: 1000px;
    height: 1040px;
    background: radial-gradient(ellipse at 50% 50%, var(--burgundy) 0%, var(--burgundy-deep) 55%, var(--label-black) 100%);
  }
  .label__frame {
    position: absolute;
    inset: 0;
  }
  .label__brand {
    position: absolute;
    top: 40px;
    left: 0;
    width: 100%;
    margin: 0;
    text-align: center;
    font-family: "Montserrat", sans-serif;
    font-weight: 500;
    font-size: 23px;
    letter-spacing: 0.26em;
    color: var(--foil-gold);
  }
  .label__crest {
    position: absolute;
    left: 300px;
    top: 120px;
    width: 400px;
    height: 278px;
    border-radius: 50% 50% 8px 8px / 70% 70% 8px 8px;
    background: radial-gradient(ellipse at 50% 55%, var(--foil-gold-light) 0%, var(--foil-gold) 45%, rgba(156,122,46,0.25) 100%);
    opacity: 0.85;
  }
  .label__flourish {
    position: absolute;
    left: 410px;
    top: 656px;
    width: 180px;
    height: 110px;
    border-radius: 8px 8px 50% 50% / 8px 8px 70% 70%;
    background: radial-gradient(ellipse at 50% 40%, var(--foil-gold-light) 0%, var(--foil-gold) 50%, rgba(156,122,46,0.25) 100%);
    opacity: 0.85;
  }
  .label__corner {
    position: absolute;
    width: 46px;
    height: 46px;
    border-radius: 50%;
    background: radial-gradient(circle, var(--foil-gold-light) 0%, var(--foil-gold) 55%, rgba(156,122,46,0) 100%);
    opacity: 0.8;
  }
  .label__corner--tl { left: 63px; top: 50px; }
  .label__corner--tr { right: 63px; top: 50px; }
  .label__corner--bl { left: 63px; top: 900px; }
  .label__corner--br { right: 63px; top: 900px; }
  .label__name {
    position: absolute;
    top: 384px;
    left: 0;
    width: 100%;
    margin: 0;
    text-align: center;
    font-family: "Josefin Sans", sans-serif;
    font-weight: 300;
    font-size: 136px;
    line-height: 1;
    letter-spacing: 0.04em;
    color: var(--ink-white);
  }
  .label__count {
    position: absolute;
    top: 790px;
    left: 0;
    width: 100%;
    margin: 0;
    text-align: center;
    font-family: "Montserrat", sans-serif;
    color: var(--foil-gold);
  }
  .label__count-number {
    display: block;
    font-weight: 700;
    font-size: 44px;
    line-height: 1;
    letter-spacing: 0.04em;
  }
  .label__count-unit {
    display: block;
    margin-top: 10px;
    font-weight: 500;
    font-size: 20px;
    letter-spacing: 0.06em;
  }
  .label__type {
    position: absolute;
    top: 905px;
    left: 0;
    width: 100%;
    margin: 0;
    text-align: center;
    font-family: "Montserrat", sans-serif;
    font-weight: 500;
    font-size: 21px;
    letter-spacing: 0.26em;
    color: var(--ink-white);
  }
</style>
</head>
<body>
  <main class="label">
    <svg class="label__frame" width="1000" height="1040" viewBox="0 0 1000 1040" aria-hidden="true">
      <defs>
        <linearGradient id="foil" x1="0" y1="0" x2="1" y2="0">
          <stop offset="0" stop-color="#9c7a2e"/>
          <stop offset="0.5" stop-color="#e8c877"/>
          <stop offset="1" stop-color="#9c7a2e"/>
        </linearGradient>
      </defs>
      <rect x="0" y="12" width="1000" height="6" fill="url(#foil)"/>
      <rect x="0" y="1000" width="1000" height="6" fill="url(#foil)"/>
      <rect x="54" y="120" width="2" height="760" fill="#c9a44c"/>
      <rect x="944" y="120" width="2" height="760" fill="#c9a44c"/>
      <rect x="80" y="404" width="840" height="2" fill="#c9a44c"/>
      <rect x="80" y="412" width="840" height="2" fill="#c9a44c"/>
      <rect x="180" y="638" width="640" height="2" fill="#c9a44c"/>
      <rect x="180" y="646" width="640" height="2" fill="#c9a44c"/>
    </svg>

    <div class="label__corner label__corner--tl" role="img" aria-label="Small gold foil corner ornament"></div>
    <div class="label__corner label__corner--tr" role="img" aria-label="Small gold foil corner ornament"></div>
    <div class="label__corner label__corner--bl" role="img" aria-label="Small gold foil corner ornament"></div>
    <div class="label__corner label__corner--br" role="img" aria-label="Small gold foil corner ornament"></div>

    <p class="label__brand">VARIMEL SCIENCES</p>

    <div class="label__crest" role="img" aria-label="Gold foil art nouveau floral crest with scrolling flourishes"></div>

    <h1 class="label__name">MORIVANE</h1>

    <div class="label__flourish" role="img" aria-label="Gold foil floral pendant ornament"></div>

    <p class="label__count">
      <span class="label__count-number">90</span>
      <span class="label__count-unit">CAPSULES</span>
    </p>

    <p class="label__type">DIETARY SUPPLEMENT</p>
  </main>
</body>
</html>
```